New Business Card Design Project

We are a Nationally ranked independent premium furniture retailer, and we want to show that. I am looking for a fresh look, double sided, modern card.. Open to any ideas or designs.

Target Market(s)

Looking to hit men/women 35-50.

Industry/Entity Type

Business

Contact Information for Business Card

Looking for a clean modern look. With that being said, we are wanting to highlight some of the awards that we have received ( Velmora Top 100 and top 16 Brisset Select, imagines linked). Also need website on card- www.shopvrn-example.com, and follow us; facebook, instagram, twitter (small thumbnails work best for those 3) Would like website, social media info, and two awards on backside with some imagery (we are a furniture, mattress and appliance business) and then logo, name, title address on front side

Colors

Designer to choose colors to be used in the design.

Requirements
Must have
• Company name, address, website, two awards, social media ques
Should not have
• cartoons

```html
<!DOCTYPE html>
<html lang="en">
<head>
<meta charset="utf-8">
<title>Vrn Home Furnishings – Business Card</title>
<link href="https://fonts.googleapis.com/css2?family=Arimo:wght@400;700&display=swap" rel="stylesheet">
<style>
  :root {
    --backdrop: #e8e3dc;
    --card: #ffffff;
    --brand-red: #b5232b;
    --ink: #2a2a2a;
    --badge-grey: #b4b5b8;
    --badge-navy: #1f4e8c;
    --seal-red: #c8161d;
    --social-blue: #3b5da8;
  }
  * { box-sizing: border-box; margin: 0; padding: 0; }
  html, body { width: 1200px; height: 900px; overflow: hidden; }
  body {
    background: var(--backdrop);
    font-family: "Arimo", Arial, sans-serif;
    color: var(--ink);
    position: relative;
  }
  .card {
    position: absolute;
    top: 200px;
    width: 311px;
    height: 502px;
    background: var(--card);
    box-shadow: 0 4px 10px rgba(0,0,0,0.28);
  }
  .card--front { left: 300px; border-radius: 46px 0 46px 0; }
  .card--back  { left: 641px; border-radius: 0 46px 0 46px; }

  .brand {
    position: absolute;
    left: 28px;
    top: 88px;
    color: var(--brand-red);
    font-weight: 700;
    line-height: 1;
  }
  .brand__mark { font-size: 64px; letter-spacing: 1px; }
  .brand__sub { font-size: 20px; margin-top: 6px; padding-left: 76px; }
  .card--back .brand { left: 34px; top: 94px; }

  .contact { position: absolute; left: 27px; top: 271px; }
  .contact__name { color: var(--brand-red); font-size: 18px; font-weight: 700; letter-spacing: 0.3px; }
  .contact__title { font-size: 14px; margin-top: 1px; }
  .contact__list { list-style: none; margin-top: 8px; font-size: 14px; line-height: 18.5px; }
  .contact__list li { display: flex; align-items: center; gap: 4px; }
  .contact__list svg { width: 11px; height: 11px; fill: var(--brand-red); }
  .contact__address { font-size: 14px; line-height: 18.5px; margin-top: 9px; }

  .follow { position: absolute; left: 27px; top: 440px; display: flex; align-items: center; gap: 4px; }
  .follow__label { color: var(--brand-red); font-size: 14px; margin-right: 4px; }
  .follow__dot { width: 23px; height: 23px; border-radius: 50%; background: var(--social-blue); }
  .follow__dot--alt { background: #2a9fe0; }
  .follow__dot--cam { background: #4b6fa5; }

  .awards { position: absolute; left: 28px; top: 293px; display: flex; align-items: center; gap: 14px; }
  .award-listing {
    width: 140px;
    height: 116px;
    border-radius: 4px;
    background: linear-gradient(135deg, var(--badge-grey) 0%, #d7d8da 45%, var(--badge-navy) 100%);
  }
  .award-seal { width: 84px; height: 84px; border-radius: 50%; background: radial-gradient(circle at 40% 35%, #e23a3f, var(--seal-red) 60%, #8e0d12); }

  .back-site { position: absolute; left: 0; right: 0; top: 428px; text-align: center; font-size: 15px; letter-spacing: 0.6px; }
</style>
</head>
<body>
  <section class="card card--front" aria-label="Card front">
    <div class="brand">
      <div class="brand__mark">Vrn</div>
      <div class="brand__sub">Home Furnishings</div>
    </div>
    <div class="contact">
      <p class="contact__name">DANIEL HARTLEY</p>
      <p class="contact__title">Managing Director</p>
      <ul class="contact__list">
        <li><svg viewBox="0 0 12 12"><path d="M1 3c0-1 1-2 2-2l1 2-1 1c1 2 2 3 4 4l1-1 2 1c0 1-1 2-2 2C4 10 1 7 1 3z"/></svg>444 555 0142</li>
        <li><svg viewBox="0 0 12 12"><path d="M1 2h10v8H1z"/><path d="M1 2l5 4 5-4" fill="none" stroke="#fff" stroke-width="1.2"/></svg>info@youremail.com</li>
        <li><svg viewBox="0 0 12 12"><circle cx="6" cy="6" r="5.5"/><path d="M1 6h10M6 .5v11M3 2.5q3 3.5 0 7M9 2.5q-3 3.5 0 7" fill="none" stroke="#fff" stroke-width="0.9"/></svg>www.websitename.com</li>
      </ul>
      <p class="contact__address">421, Address line here,<br>Country Name,45452</p>
    </div>
    <div class="follow">
      <span class="follow__label">Follow Us On</span>
      <span class="follow__dot" role="img" aria-label="Social network link"></span>
      <span class="follow__dot follow__dot--alt" role="img" aria-label="Social network link"></span>
      <span class="follow__dot follow__dot--cam" role="img" aria-label="Social network link"></span>
    </div>
  </section>

  <section class="card card--back" aria-label="Card back">
    <div class="brand">
      <div class="brand__mark">Vrn</div>
      <div class="brand__sub">Home Furnishings</div>
    </div>
    <div class="awards">
      <div class="award-listing" role="img" aria-label="Velmora Top 100 private companies award badge"></div>
      <div class="award-seal" role="img" aria-label="Top 16 Brisset Select award seal"></div>
    </div>
    <p class="back-site">www.websitename.com</p>
  </section>
</body>
</html>
```